Edgy rebranded biz cards KRB

We are rebranding our 20 yr old mortgage company with a new logo and would like cards to compliment our new look.

Target Market(s)

potential home buyers or clients for refinance

Industry/Entity Type

Mortgage Brokerage

Contact Information for Business Card

418 W. Lomita Ave #305
Henderson, NV 89152
702.519.4827 o
702-519-4829 f
www.kestrelridgelending,example
nmls 842019
KRB is an equal housing lender

Font styles to use
Sans Serif

Colors
0455a3
3176b5
0393ce
33a6d7

Requirements
Must have
• space for a photo
Nice to have
• One side with the company info and the other with the person's info

```html
<!DOCTYPE html>
<html lang="en">
<head>
<meta charset="utf-8">
<title>Kestrel Ridge Lending – Business Card</title>
<link rel="stylesheet" href="https://fonts.googleapis.com/css2?family=Montserrat:wght@600;700&family=Arimo:wght@400&display=swap">
<style>
  :root {
    --blue-deep: #0455a3;
    --blue-mid: #3176b5;
    --blue-bright: #0393ce;
    --blue-soft: #33a6d7;
    --steel: #9aa4ae;
    --ink-grey: #6b6e72;
    --rule-grey: #8a8d91;
    --paper: #ffffff;
    --stage: #e9ebee;
  }
  * { margin: 0; padding: 0; box-sizing: border-box; }
  html, body { width: 1200px; height: 900px; overflow: hidden; background: var(--stage); }
  .canvas { position: relative; width: 1200px; height: 900px; }

  .card {
    position: absolute; left: 250px; width: 700px; height: 400px;
    border-radius: 28px; overflow: hidden;
    box-shadow: 0 6px 18px rgba(0,0,0,.18);
  }
  .card--front { top: 40px; background: linear-gradient(115deg, var(--blue-deep) 0%, var(--blue-mid) 45%, #6f93b8 70%, var(--steel) 100%); }
  .card--back { top: 460px; background: var(--paper); }

  .front-facet { position: absolute; inset: 0; }
  .front-wordmark {
    position: absolute; left: 0; right: 0; top: 150px; text-align: center;
    font-family: "Montserrat", sans-serif; font-weight: 700; color: var(--paper);
    letter-spacing: 2px;
  }
  .front-wordmark .name { display: block; font-size: 52px; line-height: 1.05; }
  .front-wordmark .sub { display: block; font-size: 22px; letter-spacing: 6px; margin-top: 6px; }

  .back-wordmark {
    position: absolute; right: 130px; top: 36px; text-align: right;
    font-family: "Montserrat", sans-serif; font-weight: 700; color: var(--blue-mid);
  }
  .back-wordmark .name { display: block; font-size: 34px; line-height: 1.05; letter-spacing: 1px; }
  .back-wordmark .sub { display: block; font-size: 15px; letter-spacing: 5px; margin-top: 4px; }
  .lender-badge { position: absolute; right: 40px; top: 44px; width: 62px; height: 54px; background: #1e1e1e; border-radius: 4px; }

  .office {
    position: absolute; right: 40px; top: 118px; text-align: right; font-style: normal;
    font-family: "Arimo", sans-serif; font-size: 19px; line-height: 1.4; color: var(--ink-grey);
  }
  .divider { position: absolute; left: 40px; right: 40px; top: 224px; height: 1px; background: var(--rule-grey); }

  .full-name {
    position: absolute; left: 48px; top: 186px;
    font-family: "Montserrat", sans-serif; font-weight: 700; font-size: 28px; line-height: 34px;
    color: var(--blue-mid); letter-spacing: 1px;
  }
  .role {
    position: absolute; left: 48px; top: 232px;
    font-family: "Arimo", sans-serif; font-size: 24px; line-height: 28px; color: var(--ink-grey);
  }
  .short-rule { position: absolute; left: 48px; top: 270px; width: 250px; height: 1px; background: var(--rule-grey); }

  .contact { position: absolute; left: 48px; top: 280px; list-style: none; font-family: "Arimo", sans-serif; font-size: 20px; color: var(--ink-grey); }
  .contact li { display: flex; align-items: center; gap: 14px; height: 30px; }
  .contact svg { width: 20px; height: 20px; fill: var(--blue-mid); flex: none; }
  .contact .web { color: var(--blue-mid); }
  .contact .web span { color: var(--ink-grey); }

  .portrait {
    position: absolute; right: 40px; top: 244px; width: 110px; height: 128px;
    border-radius: 8px;
    background: linear-gradient(160deg, #d7e6f3 0%, #a9c6e2 100%);
  }
</style>
</head>
<body>
<main class="canvas">
  <section class="card card--front" aria-label="Card front">
    <svg class="front-facet" viewBox="0 0 700 400" preserveAspectRatio="none" aria-hidden="true">
      <polygon points="180,60 470,20 640,200 520,400 120,400 60,230" fill="rgba(255,255,255,.07)"/>
      <polygon points="0,260 180,60 60,230 120,400 0,400" fill="rgba(255,255,255,.05)"/>
    </svg>
    <h1 class="front-wordmark">
      <span class="name">KESTREL RIDGE</span>
      <span class="sub">LENDING</span>
    </h1>
  </section>

  <section class="card card--back" aria-label="Card back">
    <div class="back-wordmark">
      <span class="name">KESTREL RIDGE</span>
      <span class="sub">LENDING</span>
    </div>
    <div class="lender-badge" aria-label="Equal housing lender badge"></div>

    <address class="office">
      NMLS 842019<br>
      418 W. Lomita Ave #305<br>
      Henderson, NV 89152
    </address>

    <div class="divider"></div>

    <div class="full-name">DANIEL WHITFORD</div>
    <div class="role">Broker</div>
    <div class="short-rule"></div>

    <ul class="contact">
      <li>
        <svg viewBox="0 0 24 24" aria-hidden="true"><path d="M6.6 10.8a15 15 0 0 0 6.6 6.6l2.2-2.2a1 1 0 0 1 1-.25 11.4 11.4 0 0 0 3.6.57 1 1 0 0 1 1 1V20a1 1 0 0 1-1 1A17 17 0 0 1 3 4a1 1 0 0 1 1-1h3.5a1 1 0 0 1 1 1c0 1.25.2 2.45.57 3.57a1 1 0 0 1-.25 1z"/></svg>
        702.519.4827
      </li>
      <li>
        <svg viewBox="0 0 24 24" aria-hidden="true"><path d="M6 3h9l3 3v4H6zM4 11h16a2 2 0 0 1 2 2v6a2 2 0 0 1-2 2H4a2 2 0 0 1-2-2v-6a2 2 0 0 1 2-2zm3 4v3h10v-3z"/></svg>
        702-519-4829
      </li>
      <li>
        <svg viewBox="0 0 24 24" aria-hidden="true"><path d="M12 2a10 10 0 1 0 0 20 10 10 0 0 0 0-20zm0 2c.9 0 2.2 1.8 2.8 5H9.2C9.8 5.8 11.1 4 12 4zM4.3 11h3.8a20 20 0 0 0 0 2H4.3a8 8 0 0 1 0-2zm5 0h5.4a18 18 0 0 1 0 2H9.3a18 18 0 0 1 0-2zm6.6 0h3.8a8 8 0 0 1 0 2h-3.8a20 20 0 0 0 0-2zM9.2 15h5.6c-.6 3.2-1.9 5-2.8 5s-2.2-1.8-2.8-5z"/></svg>
        <span class="web"><span>www.</span>kestrelridgelending.example</span>
      </li>
    </ul>

    <div class="portrait" role="img" aria-label="Space for the broker's portrait photo"></div>
  </section>
</main>
</body>
</html>
```